Book Cover Design

Design with title UNWAVERING
Subtitle: Ways to Kindle the Spark of Resolve
Author Name: Carla Jean Morrow
Put DAILY MERIDIAN BESTSELLER at top
Shimmer design, see inspirational images attached

```html
<!DOCTYPE html>
<html lang="en">
<head>
<meta charset="utf-8">
<title>Unwavering — Book Cover</title>
<link rel="stylesheet" href="https://fonts.googleapis.com/css2?family=Oswald:wght@400;500&family=Jost:wght@400;500;600&display=swap">
<style>
  :root {
    --page-bg: #dcdcdc;
    --sky-top: #c9b3a3;
    --sky-warm: #e7c3a6;
    --sky-cool: #c9cbb8;
    --sky-glow: #f2c59e;
    --horizon: #e9b48c;
    --ground: #1c1714;
    --gold-dark: #9a6a2a;
    --gold-mid: #c8943f;
    --gold-light: #b7822f;
    --ink: #4a4a4c;
  }
  * { margin: 0; padding: 0; box-sizing: border-box; }
  html, body {
    width: 1200px;
    height: 900px;
    overflow: hidden;
    background: var(--page-bg);
  }
  .book-cover {
    position: absolute;
    left: 305px;
    top: 30px;
    width: 590px;
    height: 840px;
    overflow: hidden;
  }
  .cover-photo {
    position: absolute;
    inset: 0;
    background:
      linear-gradient(180deg,
        var(--sky-top) 0%,
        var(--sky-warm) 14%,
        var(--sky-cool) 36%,
        var(--sky-warm) 55%,
        var(--sky-glow) 70%,
        var(--horizon) 82%,
        #6b4c3a 89%,
        var(--ground) 94%,
        var(--ground) 100%);
  }
  .bestseller-banner {
    position: absolute;
    top: 46px;
    left: 0;
    right: 0;
    text-align: center;
    font-family: "Jost", sans-serif;
    font-weight: 500;
    font-size: 22px;
    letter-spacing: 0.16em;
    color: var(--ink);
  }
  .title {
    position: absolute;
    top: 128px;
    left: 0;
    right: 0;
    text-align: center;
    font-family: "Oswald", sans-serif;
    font-weight: 500;
    font-size: 100px;
    line-height: 1;
    letter-spacing: 0.03em;
    background: linear-gradient(180deg, var(--gold-mid) 0%, var(--gold-light) 45%, var(--gold-dark) 100%);
    -webkit-background-clip: text;
    background-clip: text;
    color: transparent;
  }
  .subtitle {
    position: absolute;
    top: 290px;
    left: 0;
    right: 0;
    text-align: center;
    font-family: "Jost", sans-serif;
    font-weight: 600;
    font-size: 27px;
    color: var(--ink);
  }
  .author {
    position: absolute;
    bottom: 34px;
    left: 0;
    right: 0;
    text-align: center;
    font-family: "Jost", sans-serif;
    font-weight: 600;
    font-size: 28px;
    letter-spacing: 0.2em;
    color: var(--gold-mid);
  }
</style>
</head>
<body>
  <div class="book-cover">
    <div class="cover-photo" role="img" aria-label="Photograph of a sunset sky with a lone hiker standing on a rocky ridge in silhouette"></div>
    <p class="bestseller-banner">DAILY MERIDIAN BESTSELLER</p>
    <h1 class="title">UNWAVERING</h1>
    <p class="subtitle">Ways to Kindle the Spark of Resolve</p>
    <p class="author">Carla Jean Morrow</p>
  </div>
</body>
</html>
```